I need a better looking dashboard for my web application

I have a very table heavy web page that I would like to add a design touch to it. I have the logo and primary colors picked out, I just need some help in adding visual appeal the page. I would also like to add a couple of button to the page as shortcuts. Every spot that has a + sign could have a button added. I would also like to add another graph (the data will be in the uploaded files. Please feel free to ask any questions :-)

```html
<!DOCTYPE html>
<html lang="en">
<head>
<meta charset="utf-8">
<title>ShiftCover Dashboard</title>
<link href="https://fonts.googleapis.com/css2?family=Nunito:wght@400;600;700&display=swap" rel="stylesheet">
<style>
:root{
  --bg:#eef0f4;
  --screen:#f8f8fa;
  --white:#ffffff;
  --ink:#2b2d33;
  --muted:#6f7380;
  --line:#e7e8ee;
  --purple:#6b3fb8;
  --cyan:#14a9e6;
  --green:#28c46c;
  --orange:#fb9b3e;
  --red:#ee4a55;
  --avatar:#8a8f9c;
}
*{box-sizing:border-box;margin:0;padding:0}
html,body{width:1200px;height:785px;overflow:hidden}
body{background:var(--bg);font-family:'Nunito',sans-serif;color:var(--ink)}
.board{display:grid;grid-template-columns:585px 585px;grid-template-rows:378px 378px;gap:10px;padding:10px 10px}
.screen{background:var(--screen);border-radius:8px;overflow:hidden;box-shadow:0 2px 8px rgba(30,30,60,.12);display:flex;flex-direction:column}
.topbar{height:26px;background:var(--white);display:flex;align-items:center;padding:0 8px;border-bottom:1px solid var(--line);flex:none}
.brand{display:flex;align-items:center;gap:4px;font-weight:700;font-size:10px;color:var(--cyan);width:100px}
.brand-dot{width:9px;height:9px;border-radius:50%;background:var(--cyan)}
.nav{display:flex;gap:14px;margin-left:auto;font-size:5.5px;color:var(--muted);align-items:center;height:100%}
.nav span{display:flex;align-items:center;height:100%}
.nav .active{color:var(--ink);font-weight:700;border-bottom:1.5px solid var(--cyan)}
.user{display:flex;align-items:center;gap:4px;margin-left:14px;font-size:5px;color:var(--muted);line-height:1.2}
.user b{color:var(--ink);font-weight:600;display:block}
.av{width:11px;height:11px;border-radius:50%;background:var(--avatar);display:inline-block;flex:none}
.bell{width:8px;height:8px}
.body{flex:1;display:grid;grid-template-columns:100px 1fr;min-height:0}
.sidebar{background:var(--white);border-right:1px solid var(--line);font-size:5.3px;color:var(--muted)}
.sb-head{background:var(--purple);color:#fff;font-weight:700;height:19px;display:flex;align-items:center;padding:0 8px;justify-content:space-between}
.sb-item{padding:5px 8px 5px 18px;line-height:1.3}
.sb-item.on{color:var(--ink);background:#fafafb;border-left:1.5px solid var(--cyan);margin:0 8px 0 8px;padding-left:9px}
.sb-cal{color:var(--ink);font-weight:700;padding:8px;display:flex;justify-content:space-between}
.main{padding:10px 12px;min-height:0;overflow:hidden;display:flex;flex-direction:column}
.head{display:flex;align-items:center;margin-bottom:8px}
.head h1{font-size:9px;font-weight:600}
.btn{font-size:5.3px;height:16px;padding:0 9px;border-radius:2px;display:flex;align-items:center;gap:3px}
.btn.ghost{border:1px solid var(--line);color:var(--purple);background:var(--white);margin-left:auto}
.btn.fill{background:var(--purple);color:#fff;margin-left:5px}
.summary{background:var(--white);border-radius:3px;padding:6px 6px 5px;font-size:5.3px;color:var(--muted);margin-bottom:7px;box-shadow:0 1px 2px rgba(0,0,0,.03)}
.summary .row{display:flex;justify-content:space-between;margin-bottom:5px}
.summary b{color:var(--ink)}
.bar{height:2.5px;display:flex}
.dot{display:inline-block;width:3.5px;height:3.5px;border-radius:50%;margin-right:3px;vertical-align:middle}
table{width:100%;border-collapse:collapse;background:var(--white);font-size:5.2px}
th{font-weight:600;text-align:left;color:var(--ink);padding:0 6px;height:17px;border-bottom:1px solid var(--line);border-right:1px solid var(--line)}
th:last-child{border-right:0}
td{padding:0 6px;height:22px;border-bottom:1px solid var(--line);white-space:nowrap}
.ico{width:7px;height:7px;vertical-align:middle;margin-right:5px}
.person{display:flex;align-items:center;gap:3px}
.person .av{width:8px;height:8px}
.initials{width:8px;height:8px;border-radius:50%;background:#e4e5ea;font-size:3.5px;display:inline-flex;align-items:center;justify-content:center;color:var(--muted)}
.chart-card{background:var(--white);border-radius:3px;padding:10px 10px 8px;flex:none}
.chart-card h2{font-size:5.5px;font-weight:600;text-align:center;margin-bottom:4px}
.legend{display:flex;justify-content:center;gap:14px;font-size:5.2px;margin-top:6px}
.legend i{display:inline-block;width:6px;height:6px;margin-right:4px;vertical-align:middle}
.photo{width:32px;height:32px;border:1px solid var(--red);border-radius:2px;display:block;margin:0 auto;padding:1px;background:var(--white)}
.photo span{display:block;width:100%;height:100%;border-radius:1px}
.center{text-align:center}
</style>
</head>
<body>
<svg width="0" height="0" style="position:absolute" aria-hidden="true">
  <symbol id="i-edit" viewBox="0 0 16 16"><path d="M3 13l1-4 7-7 3 3-7 7zM3 15h10" fill="none" stroke="#6b3fb8" stroke-width="1.3"/></symbol>
  <symbol id="i-trash" viewBox="0 0 16 16"><path d="M3 4h10M6 4V2h4v2M4 4l1 10h6l1-10M7 7v5M9 7v5" fill="none" stroke="#ee4a55" stroke-width="1.3"/></symbol>
  <symbol id="i-eye" viewBox="0 0 16 16"><path d="M1 8s3-5 7-5 7 5 7 5-3 5-7 5-7-5-7-5z" fill="none" stroke="#6b3fb8" stroke-width="1.3"/><circle cx="8" cy="8" r="2" fill="none" stroke="#6b3fb8" stroke-width="1.3"/></symbol>
  <symbol id="i-ok" viewBox="0 0 16 16"><circle cx="8" cy="8" r="6.5" fill="none" stroke="#14a9e6" stroke-width="1.3"/><path d="M5 8l2 2 4-4" fill="none" stroke="#14a9e6" stroke-width="1.3"/></symbol>
  <symbol id="i-no" viewBox="0 0 16 16"><circle cx="8" cy="8" r="6.5" fill="none" stroke="#ee4a55" stroke-width="1.3"/><path d="M5.5 5.5l5 5M10.5 5.5l-5 5" fill="none" stroke="#ee4a55" stroke-width="1.3"/></symbol>
  <symbol id="i-bell" viewBox="0 0 16 16"><path d="M4 11V7a4 4 0 018 0v4l1 1H3zM7 14h2" fill="none" stroke="#2b2d33" stroke-width="1.3"/><circle cx="13" cy="3" r="2" fill="#14a9e6"/></symbol>
  <symbol id="i-filter" viewBox="0 0 16 16"><path d="M2 5h12M2 11h12" stroke="#6b3fb8" stroke-width="1.3"/><circle cx="6" cy="5" r="1.8" fill="#fff" stroke="#6b3fb8"/><circle cx="10" cy="11" r="1.8" fill="#fff" stroke="#6b3fb8"/></symbol>
  <symbol id="i-plus" viewBox="0 0 16 16"><circle cx="8" cy="8" r="6.5" fill="none" stroke="#fff" stroke-width="1.3"/><path d="M8 5v6M5 8h6" stroke="#fff" stroke-width="1.3"/></symbol>
</svg>

<div class="board">

<!-- Managed openings -->
<section class="screen">
  <header class="topbar">
    <div class="brand"><span class="brand-dot"></span>ShiftCover</div>
    <nav class="nav"><span class="active">Home</span><span>Demo Outbox</span><span>Location Admin ⌄</span><span>Regular Staff ⌄</span><svg class="bell"><use href="#i-bell"/></svg></nav>
    <div class="user"><span class="av" role="img" aria-label="User avatar"></span><div><b>John Doe</b>Manager</div></div>
  </header>
  <div class="body">
    <aside class="sidebar">
      <div class="sb-head"><span>◎ Dashboard</span><span>⌄</span></div>
      <div class="sb-item on">Managed Openings</div>
      <div class="sb-item">Regular Staff Leave<br>Requests</div>
      <div class="sb-item">My Leave Requests</div>
      <div class="sb-item">Location Overview</div>
      <div class="sb-item">Pending Profile Images</div>
      <div class="sb-item">Substitute Attendance</div>
      <div class="sb-cal"><span>▦ Calendar</span><span>›</span></div>
    </aside>
    <main class="main">
      <div class="head"><h1>Managed Openings</h1><span class="btn ghost"><svg class="ico" style="margin:0"><use href="#i-filter"/></svg>Filters</span><span class="btn fill"><svg class="ico" style="margin:0"><use href="#i-plus"/></svg>Create New</span></div>
      <div class="summary">
        <div class="row"><span>Total: <b>20</b></span><span><span class="dot" style="background:var(--cyan)"></span>Available: <b>19</b> &nbsp; <span class="dot" style="background:var(--green)"></span>Assigned: <b>1</b></span></div>
        <div class="bar"><span style="flex:19;background:var(--cyan)"></span><span style="flex:1;background:var(--green)"></span></div>
      </div>
      <table>
        <tr><th>STATUS ↓</th><th>CATEGORY</th><th>REGULAR STAFF</th><th>SUMMARY</th><th>LOCATION</th><th>TIME SLOTS SUMMARY</th><th>OPTIONS</th></tr>
        <tr><td><span class="dot" style="background:var(--green)"></span>Assigned</td><td>Food Service</td><td>Extra Duty</td><td>Immediate Need! Lorem Ipsum</td><td>LJE</td><td>12/30 - 01/01 (2h 30m)</td><td><svg class="ico"><use href="#i-edit"/></svg><svg class="ico"><use href="#i-trash"/></svg></td></tr>
        <tr><td><span class="dot" style="background:var(--cyan)"></span>Available</td><td>Teacher</td><td><span class="person"><span class="av" role="img" aria-label="Staff photo"></span>Naomi Willis</span></td><td>Immediate Need! Dolor Amet</td><td>WDMS</td><td>02/12 - 02/16 (4h 10m)</td><td><svg class="ico"><use href="#i-edit"/></svg><svg class="ico"><use href="#i-trash"/></svg></td></tr>
        <tr><td><span class="dot" style="background:var(--cyan)"></span>Available</td><td>Bus Driver</td><td>Extra Duty</td><td>Immediate Need! Consectetur...</td><td>WDMS</td><td>02/03 - 02/07 (4h 10m)</td><td><svg class="ico"><use href="#i-edit"/></svg><svg class="ico"><use href="#i-trash"/></svg></td></tr>
        <tr><td><span class="dot" style="background:var(--cyan)"></span>Available</td><td>Custodian</td><td>Extra Duty</td><td>Seeking Sub for Lorem Ipsum</td><td>FMS</td><td>01/06 - 01/10 (3h 50m)</td><td><svg class="ico"><use href="#i-edit"/></svg><svg class="ico"><use href="#i-trash"/></svg></td></tr>
        <tr><td><span class="dot" style="background:var(--cyan)"></span>Available</td><td>Teacher's Aide</td><td>Extra Duty</td><td>Seeking Sub for IT</td><td>FMS</td><td>01/20 - 01/23 (3h 20m)</td><td><svg class="ico"><use href="#i-edit"/></svg><svg class="ico"><use href="#i-trash"/></svg></td></tr>
        <tr><td><span class="dot" style="background:var(--cyan)"></span>Available</td><td>Food Service</td><td><span class="person"><span class="av" role="img" aria-label="Staff photo"></span>Gladys Richardson</span></td><td>Seeking Sub for SS</td><td>FMS</td><td>01/20 - 01/05 (3h 20m)</td><td><svg class="ico"><use href="#i-edit"/></svg><svg class="ico"><use href="#i-trash"/></svg></td></tr>
        <tr><td><span class="dot" style="background:var(--cyan)"></span>Available</td><td>Teacher's Aide</td><td><span class="person"><span class="av" role="img" aria-label="Staff photo"></span>Alan Bowman</span></td><td>Substitue Needed for Lorem I...</td><td>LJE</td><td>01/20 - 01/05 (3h 20m)</td><td><svg class="ico"><use href="#i-edit"/></svg><svg class="ico"><use href="#i-trash"/></svg></td></tr>
        <tr><td><span class="dot" style="background:var(--cyan)"></span>Available</td><td>Bus Driver</td><td>Extra Duty</td><td>Immediate Need! Consectetur...</td><td>WDMS</td><td>02/03 - 02/07 (4h 10m)</td><td><svg class="ico"><use href="#i-edit"/></svg><svg class="ico"><use href="#i-trash"/></svg></td></tr>
        <tr><td><span class="dot" style="background:var(--cyan)"></span>Available</td><td>Custodian</td><td>Extra Duty</td><td>Seeking Sub for Lorem Ipsum</td><td>FMS</td><td>01/06 - 01/10 (3h 50m)</td><td><svg class="ico"><use href="#i-edit"/></svg><svg class="ico"><use href="#i-trash"/></svg></td></tr>
      </table>
    </main>
  </div>
</section>

<!-- Leave requests -->
<section class="screen">
  <header class="topbar">
    <div class="brand"><span class="brand-dot"></span>ShiftCover</div>
    <nav class="nav"><span class="active">Home</span><span>Demo Outbox</span><span>Location Admin ⌄</span><span>Regular Staff ⌄</span><svg class="bell"><use href="#i-bell"/></svg></nav>
    <div class="user"><span class="av" role="img" aria-label="User avatar"></span><div><b>John Doe</b>Manager</div></div>
  </header>
  <div class="body">
    <aside class="sidebar">
      <div class="sb-head"><span>◎ Dashboard</span><span>⌄</span></div>
      <div class="sb-item">Managed Openings</div>
      <div class="sb-item on">Regular Staff Leave<br>Requests</div>
      <div class="sb-item">My Leave Requests</div>
      <div class="sb-item">Location Overview</div>
      <div class="sb-item">Pending Profile Images</div>
      <div class="sb-item">Substitute Attendance</div>
      <div class="sb-cal"><span>▦ Calendar</span><span>›</span></div>
    </aside>
    <main class="main">
      <div class="head"><h1>Regular Staff Leave Requests</h1><span class="btn ghost"><svg class="ico" style="margin:0"><use href="#i-filter"/></svg>Filters</span><span class="btn fill"><svg class="ico" style="margin:0"><use href="#i-plus"/></svg>Create New</span></div>
      <div class="summary">
        <div class="row"><span>Total: <b>20</b></span><span><span class="dot" style="background:var(--orange)"></span>Pending: <b>20</b></span></div>
        <div class="bar" style="background:var(--orange)"></div>
      </div>
      <table>
        <tr><th rowspan="2">STATUS ↓</th><th rowspan="2">FULL NAME</th><th colspan="2" class="center" style="height:14px">LOCATION</th><th rowspan="2">TIME SLOTS SUMMARY</th><th rowspan="2">OPTIONS</th></tr>
        <tr><th style="height:14px">ASSIGNMENT</th><th style="height:14px">PREARRANGED SUB</th></tr>
        <tr><td><span class="dot" style="background:var(--orange)"></span>Pending</td><td><span class="person"><span class="av" role="img" aria-label="Staff photo"></span>Alan Bowman</span></td><td>N/A</td><td>N/A</td><td>12/22 - 12/22 (0h 30m)</td><td><svg class="ico"><use href="#i-edit"/></svg><svg class="ico"><use href="#i-eye"/></svg></td></tr>
        <tr><td><span class="dot" style="background:var(--orange)"></span>Pending</td><td><span class="person"><span class="av" role="img" aria-label="Staff photo"></span>Jeremy Gardner</span></td><td>N/A</td><td>N/A</td><td>12/24 - 12/30 (4h 45m)</td><td><svg class="ico"><use href="#i-edit"/></svg><svg class="ico"><use href="#i-eye"/></svg></td></tr>
        <tr><td><span class="dot" style="background:var(--orange)"></span>Pending</td><td><span class="person"><span class="initials">SC</span>Scarlet Cook</span></td><td>Counselor</td><td></td><td>12/20 - 12/31 (4h 45m)</td><td><svg class="ico"><use href="#i-edit"/></svg><svg class="ico"><use href="#i-eye"/></svg></td></tr>
        <tr><td><span class="dot" style="background:var(--orange)"></span>Pending</td><td><span class="person"><span class="av" role="img" aria-label="Staff photo"></span>Hannah Collins</span></td><td>N/A</td><td>N/A</td><td>12/20 - 01/09 (1h 45m)</td><td><svg class="ico"><use href="#i-edit"/></svg><svg class="ico"><use href="#i-eye"/></svg></td></tr>
        <tr><td><span class="dot" style="background:var(--orange)"></span>Pending</td><td><span class="person"><span class="av" role="img" aria-label="Staff photo"></span>Monica Mason</span></td><td>Administrator</td><td><span class="person"><span class="av" role="img" aria-label="Substitute photo"></span>Ian Robertson</span></td><td>12/24 - 01/16 (5h 0m)</td><td><svg class="ico"><use href="#i-edit"/></svg><svg class="ico"><use href="#i-eye"/></svg></td></tr>
        <tr><td><span class="dot" style="background:var(--orange)"></span>Pending</td><td><span class="person"><span class="av" role="img" aria-label="Staff photo"></span>Gladys Herrera</span></td><td>Administrator</td><td></td><td>12/20 - 01/04 (2h 0m)</td><td><svg class="ico"><use href="#i-edit"/></svg><svg class="ico"><use href="#i-eye"/></svg></td></tr>
        <tr><td><span class="dot" style="background:var(--orange)"></span>Pending</td><td><span class="person"><span class="av" role="img" aria-label="Staff photo"></span>Alan Bowman</span></td><td>N/A</td><td>N/A</td><td>12/22 - 12/22 (0h 30m)</td><td><svg class="ico"><use href="#i-edit"/></svg><svg class="ico"><use href="#i-eye"/></svg></td></tr>
        <tr><td><span class="dot" style="background:var(--orange)"></span>Pending</td><td><span class="person"><span class="av" role="img" aria-label="Staff photo"></span>Jeremy Gardner</span></td><td>N/A</td><td>N/A</td><td>12/24 - 12/30 (4h 45m)</td><td><svg class="ico"><use href="#i-edit"/></svg><svg class="ico"><use href="#i-eye"/></svg></td></tr>
      </table>
    </main>
  </div>
</section>

<!-- Location overview -->
<section class="screen">
  <header class="topbar">
    <div class="brand"><span class="brand-dot"></span>ShiftCover</div>
    <nav class="nav"><span class="active">Home</span><span>Demo Outbox</span><span>Location Admin ⌄</span><span>Regular Staff ⌄</span><svg class="bell"><use href="#i-bell"/></svg></nav>
    <div class="user"><span class="av" role="img" aria-label="User avatar"></span><div><b>John Doe</b>Manager</div></div>
  </header>
  <div class="body">
    <aside class="sidebar">
      <div class="sb-head"><span>◎ Dashboard</span><span>⌄</span></div>
      <div class="sb-item">Managed Openings</div>
      <div class="sb-item">Regular Staff Leave<br>Requests</div>
      <div class="sb-item">My Leave Requests</div>
      <div class="sb-item on">Location Overview</div>
      <div class="sb-item">Pending Profile Images</div>
      <div class="sb-item">Substitute Attendance</div>
      <div class="sb-cal"><span>▦ Calendar</span><span>›</span></div>
    </aside>
    <main class="main">
      <div class="head"><h1>Location Overview</h1><span class="btn ghost"><svg class="ico" style="margin:0"><use href="#i-filter"/></svg>Filters</span></div>
      <div class="chart-card">
        <h2>Leave Request / Openings / Assignments</h2>
        <svg width="440" height="180" viewBox="0 0 440 180" font-family="Nunito, sans-serif" font-size="5" fill="#6f7380">
          <g stroke="#e7e8ee" stroke-width=".6">
            <line x1="14" y1="10" x2="438" y2="10"/><line x1="14" y1="41" x2="438" y2="41"/><line x1="14" y1="72" x2="438" y2="72"/><line x1="14" y1="103" x2="438" y2="103"/><line x1="14" y1="134" x2="438" y2="134"/><line x1="14" y1="165" x2="438" y2="165"/>
          </g>
          <text x="2" y="12">10</text><text x="5" y="43">8</text><text x="5" y="74">6</text><text x="5" y="105">4</text><text x="5" y="136">2</text><text x="5" y="167">0</text>
          <rect x="52" y="118.5" width="25" height="46.5" fill="#14a9e6"/><rect x="52" y="103" width="25" height="15.5" fill="#28c46c"/>
          <rect x="80" y="103" width="25" height="62" fill="#fb9b3e"/>
          <rect x="189" y="87.5" width="25" height="77.5" fill="#14a9e6"/>
          <rect x="217" y="103" width="25" height="62" fill="#fb9b3e"/>
          <rect x="326" y="72" width="25" height="93" fill="#14a9e6"/>
          <rect x="354" y="10" width="25" height="155" fill="#fb9b3e"/>
          <text x="78" y="174" text-anchor="middle">Lake Jonas Elementary</text>
          <text x="215" y="174" text-anchor="middle">Feestberg Middle School</text>
          <text x="352" y="174" text-anchor="middle">West Devante Middle School</text>
        </svg>
        <div class="legend"><span><i style="background:var(--cyan)"></i>Openings - Unfilled</span><span><i style="background:var(--green)"></i>Openings - Filled</span><span><i style="background:var(--orange)"></i>Leave Requests - Pending</span></div>
      </div>
    </main>
  </div>
</section>

<!-- Pending profile images -->
<section class="screen">
  <header class="topbar">
    <div class="brand"><span class="brand-dot"></span>ShiftCover</div>
    <nav class="nav"><span class="active">Home</span><span>Demo Outbox</span><span>Location Admin ⌄</span><span>Regular Staff ⌄</span><svg class="bell"><use href="#i-bell"/></svg></nav>
    <div class="user"><span class="av" role="img" aria-label="User avatar"></span><div><b>John Doe</b>Manager</div></div>
  </header>
  <div class="body">
    <aside class="sidebar">
      <div class="sb-head"><span>◎ Dashboard</span><span>⌄</span></div>
      <div class="sb-item">Managed Openings</div>
      <div class="sb-item">Regular Staff Leave<br>Requests</div>
      <div class="sb-item">My Leave Requests</div>
      <div class="sb-item">Location Overview</div>
      <div class="sb-item on">Pending Profile Images</div>
      <div class="sb-item">Substitute Attendance</div>
      <div class="sb-cal"><span>▦ Calendar</span><span>›</span></div>
    </aside>
    <main class="main">
      <div class="head"><h1>Pending Profile Images</h1><span class="btn ghost"><svg class="ico" style="margin:0"><use href="#i-filter"/></svg>Filters</span></div>
      <div class="summary">
        <div class="row"><span>Total: <b>9</b></span><span><span class="dot" style="background:var(--red)"></span>Unverified <b>9</b></span></div>
        <div class="bar" style="background:var(--red)"></div>
      </div>
      <table>
        <tr><th rowspan="2">LAST NAME ↓</th><th rowspan="2">FIRST NAME</th><th colspan="2" class="center" style="height:14px">PROFILE IMAGES</th><th rowspan="2">OPTIONS</th></tr>
        <tr><th class="center" style="height:14px">PENDING</th><th class="center" style="height:14px">PREVIOUSLY VERIFIED</th></tr>
        <tr><td style="height:43px">Morales</td><td>June</td><td><span class="photo"><span role="img" aria-label="Pending profile photo of June Morales" style="background:linear-gradient(135deg,#c9a88a,#6e5440)"></span></span></td><td class="center">N/A</td><td><svg class="ico"><use href="#i-ok"/></svg><svg class="ico"><use href="#i-no"/></svg></td></tr>
        <tr><td style="height:43px">Stephens</td><td>Priscilia</td><td><span class="photo"><span role="img" aria-label="Pending profile photo of Priscilia Stephens" style="background:linear-gradient(135deg,#e7d6cc,#b9583d)"></span></span></td><td class="center">N/A</td><td><svg class="ico"><use href="#i-ok"/></svg><svg class="ico"><use href="#i-no"/></svg></td></tr>
        <tr><td style="height:43px">Stevens</td><td>Mason</td><td><span class="photo"><span role="img" aria-label="Pending profile photo of Mason Stevens" style="background:linear-gradient(135deg,#b8bcc2,#3f4550)"></span></span></td><td class="center">N/A</td><td><svg class="ico"><use href="#i-ok"/></svg><svg class="ico"><use href="#i-no"/></svg></td></tr>
        <tr><td style="height:43px">Walters</td><td>Kim</td><td><span class="photo"><span role="img" aria-label="Pending profile photo of Kim Walters" style="background:linear-gradient(135deg,#9ec3df,#3a2f2c)"></span></span></td><td class="center">N/A</td><td><svg class="ico"><use href="#i-ok"/></svg><svg class="ico"><use href="#i-no"/></svg></td></tr>
        <tr><td style="height:43px">Wills</td><td>Naomi</td><td><span class="photo"><span role="img" aria-label="Pending profile photo of Naomi Wills" style="background:linear-gradient(135deg,#5f7e84,#c7a58c)"></span></span></td><td class="center">N/A</td><td><svg class="ico"><use href="#i-ok"/></svg><svg class="ico"><use href="#i-no"/></svg></td></tr>
      </table>
    </main>
  </div>
</section>

</div>
</body>
</html>
```